Stylish Business Card for Modern hair salon

I need a simple business card design using our salon logo and colours that are in the logo. We service clients of all ages but predominantly those in the 18 to 55 age range. We have a young staff and are looking to have a card that will present a modern and clean image that represents who we are. The card should be in black and white same as our logo. Minimal use of other colours is allowed.

Industry/Entity Type

Hair And Beauty

Contact Information for Business Card

The design should have the following information
salon name - TR Hair Studio
address - 2751 Birchfield Rd.E. Mississauga, ON L7P3K2
phone - 905 614-2870
website - trhairexample.ca
instagram - tr.hairstudio
twitter - @TR_HairStudio

Colors
000000
ffffff
474747

Requirements
Must have
• simple design, salon name, address, phone, website, instagram, twitter info
• Back of card should have the following:
• YOUR NEXT APPOINTMENT
• DATE
• TIME
Nice to have
• simple design, clear to see and read,
• predominantly black and white colour, minimal use of other colours is ok
Should not have
• many colours, various fonts

```html
<!DOCTYPE html>
<html lang="en">
<head>
<meta charset="utf-8">
<title>TR Hair Studio – Business Card</title>
<link rel="stylesheet" href="https://fonts.googleapis.com/css2?family=Michroma&family=Montserrat:wght@400;600&display=swap">
<style>
  :root {
    --black: #000000;
    --white: #ffffff;
    --grey: #474747;
    --backdrop: #e4e4e4;
  }
  * { box-sizing: border-box; margin: 0; padding: 0; }
  html, body { width: 1200px; height: 1000px; overflow: hidden; }
  body {
    background: var(--backdrop);
    font-family: "Montserrat", sans-serif;
    position: relative;
  }
  .card {
    position: absolute;
    left: 220px;
    width: 760px;
    height: 430px;
    overflow: hidden;
    box-shadow: 0 6px 18px rgba(0,0,0,0.18);
  }
  .card--front { top: 40px; background: var(--white); }
  .card--back { top: 520px; background: var(--black); }

  .front-art { position: absolute; inset: 0; }

  .brand-mark {
    position: absolute;
    color: var(--white);
    font-family: "Montserrat", sans-serif;
    font-weight: 600;
    letter-spacing: 4px;
    display: flex;
    align-items: center;
    gap: 12px;
  }
  .brand-mark__square {
    width: 12px; height: 12px;
    background: var(--white);
  }
  .card--front .brand-mark { left: 44px; top: 26px; font-size: 30px; }

  .studio-name {
    position: absolute;
    left: 40px; top: 182px;
    font-family: "Michroma", sans-serif;
    font-size: 32px;
    font-weight: 400;
    color: var(--black);
    white-space: nowrap;
  }

  .contact-bar {
    position: absolute;
    height: 32px;
    background: var(--grey);
    color: var(--white);
    font-size: 13px;
    letter-spacing: 1.5px;
    display: flex;
    align-items: center;
    padding-left: 26px;
    clip-path: polygon(0 0, calc(100% - 18px) 0, 100% 100%, 18px 100%);
    white-space: nowrap;
  }
  .contact-bar--address { left: 40px; top: 378px; width: 400px; font-size: 12.5px; letter-spacing: 1.2px; }
  .contact-bar--phone { left: 490px; top: 250px; width: 250px; }
  .contact-bar--web { left: 490px; top: 292px; width: 250px; }
  .contact-bar--insta { left: 490px; top: 334px; width: 250px; }
  .contact-bar--handle { left: 490px; top: 376px; width: 250px; }

  .contact-icon { position: absolute; width: 18px; height: 18px; }

  .back-band {
    position: absolute;
    left: 0; right: 0; bottom: 0;
    height: 170px;
    background: var(--grey);
    color: var(--white);
  }
  .card--back .brand-mark {
    left: 0; right: 0; top: 100px;
    justify-content: center;
    font-size: 38px;
  }
  .appointment-title {
    position: absolute;
    top: 24px; left: 0; right: 0;
    text-align: center;
    font-size: 20px;
    font-weight: 600;
    letter-spacing: 5px;
  }
  .appointment-field {
    position: absolute;
    top: 100px;
    font-size: 13px;
    letter-spacing: 2px;
    display: flex;
    align-items: flex-end;
    gap: 12px;
  }
  .appointment-field__line {
    display: inline-block;
    width: 200px;
    border-bottom: 1px solid var(--white);
  }
  .appointment-field--date { left: 60px; }
  .appointment-field--time { left: 430px; }
</style>
</head>
<body>

<section class="card card--front" aria-label="Business card front">
  <svg class="front-art" width="760" height="430" viewBox="0 0 760 430" aria-hidden="true">
    <polygon points="0,0 760,0 760,230 0,100" fill="var(--black)"/>
    <line x1="0" y1="106" x2="760" y2="236" stroke="var(--black)" stroke-width="1.5" stroke-dasharray="4 4"/>
  </svg>

  <div class="brand-mark"><span class="brand-mark__square"></span>TR Hair</div>

  <h1 class="studio-name">TR Hair Studio</h1>

  <svg class="contact-icon" style="left:40px;top:340px" viewBox="0 0 18 18" aria-label="Address">
    <path d="M9 1.5a5 5 0 0 0-5 5c0 3.8 5 10 5 10s5-6.2 5-10a5 5 0 0 0-5-5z" fill="none" stroke="var(--black)" stroke-width="1.5"/>
    <circle cx="9" cy="6.5" r="1.8" fill="var(--black)"/>
  </svg>
  <div class="contact-bar contact-bar--address">2751 Birchfield Rd.E. Mississauga, ON L7P3K2</div>

  <svg class="contact-icon" style="left:464px;top:257px" viewBox="0 0 18 18" aria-label="Phone">
    <rect x="4.5" y="1" width="9" height="16" rx="1.5" fill="none" stroke="var(--black)" stroke-width="1.5"/>
    <line x1="7.5" y1="14.5" x2="10.5" y2="14.5" stroke="var(--black)" stroke-width="1.2"/>
  </svg>
  <div class="contact-bar contact-bar--phone">905 614-2870</div>

  <svg class="contact-icon" style="left:464px;top:299px" viewBox="0 0 18 18" aria-label="Website">
    <circle cx="9" cy="9" r="7.5" fill="none" stroke="var(--black)" stroke-width="1.4"/>
    <ellipse cx="9" cy="9" rx="3.2" ry="7.5" fill="none" stroke="var(--black)" stroke-width="1.1"/>
    <line x1="1.5" y1="9" x2="16.5" y2="9" stroke="var(--black)" stroke-width="1.1"/>
  </svg>
  <div class="contact-bar contact-bar--web">trhairexample.ca</div>

  <svg class="contact-icon" style="left:464px;top:341px" viewBox="0 0 18 18" aria-label="Photo profile">
    <rect x="2" y="2" width="14" height="14" fill="none" stroke="var(--black)" stroke-width="1.5"/>
  </svg>
  <div class="contact-bar contact-bar--insta">tr.hairstudio</div>

  <svg class="contact-icon" style="left:464px;top:383px" viewBox="0 0 18 18" aria-label="Social handle">
    <circle cx="9" cy="9" r="7" fill="var(--black)"/>
  </svg>
  <div class="contact-bar contact-bar--handle">@TR_HairStudio</div>
</section>

<section class="card card--back" aria-label="Business card back">
  <div class="brand-mark"><span class="brand-mark__square"></span>TR Hair</div>

  <div class="back-band">
    <h2 class="appointment-title">YOUR NEXT APPOINTMENT</h2>
    <div class="appointment-field appointment-field--date">DATE <span class="appointment-field__line"></span></div>
    <div class="appointment-field appointment-field--time">TIME <span class="appointment-field__line"></span></div>
  </div>
</section>

</body>
</html>
```